KWT Contracting services . Building and maintenance services, optic fibre installation

Business cards and logo design.I need a logo that I can use on business cards ,workwear and on my vehicles. I would like the KWT to be the main or larger text and contracting services to be the smaller or less important text.I like monograms, modern designs and repeating patterns symbols. I am also a Gemini and my favourite number is 22 so if this can be any inspiration to help with the design. Am thinking of the using German flag colours as a his is my family’s heritage. And the other 2 main colours I wear is black and white.But any ideas are appreciated.I do not need a design that is trade specific but a design that could be used for any business.

Target Market(s)

General public

Contact Information for Business Card

KWT Contracting Services ( front of business card)

(Back of business card)
Milo Brackwood
0471539264
Maintenance services
Optic fibre and data installation

Logo Text

Logo can just be pattern or monogram or incorporate KWT . I like the gemini star sign and the number 22

Colors
ec1f27
000000
fbee3e
ffffff

Requirements
Must have
• Logo and KWT Contracting Services on the front of business card
Nice to have
• Possible use of German flag colours.
• Modern design.
• Design to be able to be used on black or white background as I want to put it on clothing

```html
<!DOCTYPE html>
<html lang="en">
<head>
<meta charset="utf-8">
<title>KWT Contracting Services – Business Cards</title>
<link rel="stylesheet" href="https://fonts.googleapis.com/css2?family=Montserrat:wght@400;500;700;800&display=swap">
<style>
  :root {
    --red: #ec1f27;
    --black: #000000;
    --yellow: #fbee3e;
    --white: #ffffff;
    --ink: #1a1a1a;
    --stage: #5b5b5d;
    --card-w: 620px;
    --card-h: 354px;
  }
  * { box-sizing: border-box; margin: 0; padding: 0; }
  html, body { width: 1200px; height: 880px; overflow: hidden; }
  body {
    background: var(--stage);
    font-family: "Montserrat", Arial, sans-serif;
    display: flex; flex-direction: column; align-items: center; justify-content: center;
    gap: 60px;
  }
  .card {
    position: relative;
    width: var(--card-w); height: var(--card-h);
    border-radius: 26px;
    overflow: hidden;
  }

  /* Front */
  .card--front {
    background: var(--black);
    display: flex; flex-direction: column; align-items: center; justify-content: center;
    gap: 18px;
  }
  .brand-mark { display: flex; align-items: center; gap: 14px; }
  .brand-mark__square { width: 18px; height: 18px; background: var(--yellow); }
  .brand-mark__square--red { background: var(--red); }
  .brand-mark__name {
    font-size: 84px; font-weight: 800; letter-spacing: 2px;
    color: var(--red); line-height: 1;
  }
  .front-title {
    color: var(--white); font-size: 30px; font-weight: 700;
    letter-spacing: 3px; text-transform: uppercase; text-align: center;
  }
  .front-tagline {
    display: flex; align-items: center; gap: 12px;
    color: var(--red); font-size: 13px; font-weight: 500;
    letter-spacing: 7px; text-transform: uppercase;
  }
  .front-tagline__rule { width: 110px; height: 2px; background: var(--yellow); }

  /* Back */
  .card--back { background: var(--white); }
  .back-accent {
    position: absolute; left: 0; top: 46px;
    width: 8px; height: 40px; background: var(--yellow);
  }
  .contact-block {
    position: absolute; left: 36px; top: 40px;
    color: var(--ink);
  }
  .contact-block__name {
    color: var(--red); font-size: 27px; font-weight: 700;
    text-transform: uppercase; letter-spacing: 0.5px; line-height: 1.1;
  }
  .contact-block__role { font-size: 15px; margin-top: 2px; }
  .contact-block__services { font-size: 14px; line-height: 1.4; margin-top: 14px; }
  .contact-block__address { font-size: 14px; line-height: 1.4; margin-top: 14px; }
  .contact-list { list-style: none; font-size: 14px; margin-top: 8px; line-height: 1.6; }
  .contact-list li { display: flex; align-items: center; gap: 8px; }
  .contact-list svg { width: 13px; height: 13px; fill: var(--red); flex: none; }

  .back-brand {
    position: absolute; right: 48px; top: 80px;
    display: flex; align-items: center; gap: 12px;
  }
  .back-brand .brand-mark__name { color: var(--black); font-size: 90px; }

  .back-stripe { position: absolute; left: 0; bottom: 0; width: 100%; height: 120px; }
</style>
</head>
<body>

  <section class="card card--front" aria-label="Business card front">
    <div class="brand-mark">
      <span class="brand-mark__square"></span>
      <span class="brand-mark__name">KWT</span>
    </div>
    <h1 class="front-title">KWT Contracting</h1>
    <div class="front-tagline">
      <span class="front-tagline__rule"></span>
      <span>Services</span>
      <span class="front-tagline__rule"></span>
    </div>
  </section>

  <section class="card card--back" aria-label="Business card back">
    <span class="back-accent"></span>
    <div class="contact-block">
      <h2 class="contact-block__name">Milo Brackwood</h2>
      <p class="contact-block__role">Founder &amp; CEO</p>
      <p class="contact-block__services">Maintenance services<br>Optic fibre and data installation</p>
      <p class="contact-block__address">Harbor Point 4<br>1750 Alder Crest Way<br>Fairmont, CA</p>
      <ul class="contact-list">
        <li><svg viewBox="0 0 24 24"><path d="M6.6 10.8a15 15 0 0 0 6.6 6.6l2.2-2.2a1 1 0 0 1 1-.25 11.4 11.4 0 0 0 3.6.6 1 1 0 0 1 1 1V20a1 1 0 0 1-1 1A17 17 0 0 1 3 4a1 1 0 0 1 1-1h3.5a1 1 0 0 1 1 1c0 1.250.2 2.450.6 3.6a1 1 0 0 1-.25 1z"/></svg>0471539264</li>
        <li><svg viewBox="0 0 24 24"><path d="M2 5h20v14H2z M2 5l10 8 10-8" stroke="#fff" stroke-width="1.5"/></svg>info@kwtcontracting.com</li>
        <li><svg viewBox="0 0 24 24"><circle cx="12" cy="12" r="10"/><path d="M2 12h20M12 2c3 3 3 17 0 20M12 2c-3 3-3 17 0 20" stroke="#fff" stroke-width="1.4" fill="none"/></svg>www.kwtcontracting.com</li>
      </ul>
    </div>

    <div class="back-brand">
      <span class="brand-mark__square brand-mark__square--red"></span>
      <span class="brand-mark__name">KWT</span>
    </div>

    <svg class="back-stripe" viewBox="0 0 620 120" preserveAspectRatio="none" aria-hidden="true">
      <polygon points="0,112 480,84 480,92 0,120" fill="#ec1f27"/>
      <polygon points="488,83 620,75 620,83 488,91" fill="#000000"/>
    </svg>
  </section>

</body>
</html>
```